Crispy Jerky Packaging for KO.MU

We need packaging for for our hand-crafted crispy beef jerky. We are launching a new product that is like eating a potato chip, but made of beef/pork. We would like to have a window for people to be able to see our product. It is a new type of jerky, so we need the audience to be able to see that they are getting value for what they are paying for. Where a traditional 1oz portion of jerky would have 10-11g protein, ours has 20g of protein. It is also easy on the jaw because there is no tearing off of the jerky, it eats just like a chip
Updates

Target Market(s)

Beer lovers/ health-conscious/ millenials

Industry/Entity Type

Product

Font styles to use
Other font styles liked:
• be creative

Colors
fbed22
9bcb3b
85cae6

Requirements
Must have
• Yellow packaging base
• 20g Protein per serving
• Made in Hawaii
Nice to have
• Would prefer the current font we have for the company name, KO.MU
Should not have
• cows

```html
<!DOCTYPE html>
<html lang="en">
<head>
<meta charset="utf-8">
<title>KO.MU Jerky – Pouch Front</title>
<link rel="stylesheet" href="https://fonts.googleapis.com/css2?family=Montserrat:wght@700&family=Oswald:wght@400&family=Norican&family=Questrial&display=swap">
<style>
  :root {
    --stage: #f3f5f4;
    --yellow: #fbed22;
    --green: #9bcb3b;
    --blue: #85cae6;
    --lime: #c4dc3c;
    --white: #ffffff;
    --forest: #3d6b2a;
    --ink-green: #3f6a35;
    --jerky-dark: #3a1f1e;
    --jerky-mid: #6b3a30;
  }
  * { margin: 0; padding: 0; box-sizing: border-box; }
  html, body {
    width: 1200px;
    height: 852px;
    overflow: hidden;
    background: var(--stage);
  }
  .pouch-front {
    position: absolute;
    left: 347px;
    top: 36px;
    width: 505px;
    height: 780px;
    overflow: hidden;
  }
  .pattern-field {
    position: absolute;
    inset: 0;
    background: linear-gradient(150deg,
      var(--yellow) 0%, var(--lime) 22%, var(--yellow) 40%,
      var(--blue) 58%, var(--yellow) 72%, var(--green) 100%);
  }
  .craft-note {
    position: absolute;
    left: 48px;
    top: 80px;
    width: 80px;
    font-family: "Oswald", sans-serif;
    font-size: 15px;
    line-height: 1.1;
    text-align: center;
    text-transform: uppercase;
    color: var(--ink-green);
  }
  .brand-name {
    position: absolute;
    left: 0;
    right: 0;
    top: 178px;
    text-align: center;
    font-family: "Questrial", sans-serif;
    font-weight: 400;
    font-size: 84px;
    line-height: 1;
    color: var(--white);
  }
  .product-word {
    position: absolute;
    left: 0;
    right: 0;
    top: 362px;
    text-align: center;
    font-family: "Montserrat", sans-serif;
    font-weight: 700;
    font-size: 84px;
    line-height: 1;
    color: var(--forest);
  }
  .protein-claim {
    position: absolute;
    left: 0;
    right: 0;
    top: 457px;
    text-align: center;
    font-family: "Questrial", sans-serif;
    font-size: 23px;
    color: var(--ink-green);
  }
  .product-window {
    position: absolute;
    left: 113px;
    top: 508px;
    width: 280px;
    height: 130px;
    border-radius: 18px;
    border: 6px solid rgba(255, 255, 255, 0.55);
    background: linear-gradient(110deg, var(--jerky-mid), var(--jerky-dark) 45%, var(--jerky-mid) 70%, var(--jerky-dark));
  }
  .natural-note {
    position: absolute;
    left: 0;
    right: 0;
    top: 668px;
    text-align: center;
    font-family: "Norican", cursive;
    font-size: 19px;
    color: var(--ink-green);
  }
  .origin-note {
    position: absolute;
    left: 0;
    right: 0;
    top: 700px;
    text-align: center;
    font-family: "Questrial", sans-serif;
    font-size: 22px;
    color: var(--ink-green);
  }
</style>
</head>
<body>
  <main class="pouch-front">
    <div class="pattern-field" role="img" aria-label="Geometric triangle pattern in yellow, lime green and sky blue"></div>
    <p class="craft-note">Hand<br>Crafted<br>Product</p>
    <h1 class="brand-name">KO.MU</h1>
    <h2 class="product-word">JERKY</h2>
    <p class="protein-claim">20g protein per serving</p>
    <div class="product-window" role="img" aria-label="Clear window showing pieces of crispy beef jerky"></div>
    <p class="natural-note">Made From Natural Ingredients</p>
    <p class="origin-note">made in hawaii</p>
  </main>
</body>
</html>
```